Developer needs a Software blog Design

I need a design for my software blog (I'm a developer). The design should include a homepage for browser and for mobile.

Following is a wireframe: https://sketchgrid.example/kQp7wz.

The sidebar can also include my picture I you think it should.

In the mobile version the about me and subscribe with email should be popup or dropdown.

I'm currently using this: http://tavelkin.inkpage.example/ which I like, but doesn't have all the component I want on the sidebar and I want something unique.

The most importnant is simple, clean and responsive.

Designs that I like:
http://blog.rupolat.example/
http://xwrt.example/layoutbazaar/?theme=fens
http://demo.skinorbit.example/#singularly

Out come should be a psd file with homepage and mobile homepage (and dropdowns variation for the mobile).

Target Market(s)

developers

Industry/Entity Type

Software

Font styles to use
Sans Serif

Requirements
Must have
• clean and simple. responsive. main post area need to be wide enough.

```html
<!DOCTYPE html>
<html lang="en">
<head>
<meta charset="utf-8">
<title>Tavelkin — Rumblings of a coder</title>
<link rel="stylesheet" href="https://fonts.googleapis.com/css2?family=Oswald:wght@500&family=Lato:wght@400;700&family=Aleo:wght@400&family=Roboto:wght@400&display=swap">
<style>
:root{
  --topbar:#34495e;
  --band:#3498db;
  --link:#2e8ee0;
  --ink:#111;
  --body:#555;
  --muted:#666;
  --white:#fff;
  --side-top:#4a5058;
  --side-mid:#2f343a;
  --side-low:#1c1f23;
}
*{margin:0;padding:0;box-sizing:border-box}
html,body{width:1038px;height:1200px;overflow:hidden;background:var(--white)}
body{position:relative;font-family:'Roboto',Arial,sans-serif}
a{color:var(--link)}
.sidebar{position:absolute;left:0;top:0;width:255px;height:1200px;overflow:hidden}
.sidebar-photo{position:absolute;inset:0;background:linear-gradient(180deg,var(--side-top) 0%,#3b4148 30%,var(--side-mid) 55%,var(--side-low) 100%)}
.avatar{position:absolute;left:74px;top:103px;width:108px;height:108px;border-radius:50%;border:3px solid var(--white);background:linear-gradient(180deg,#8a9096,#5a6066)}
.site-name{position:absolute;left:49px;top:222px;font-family:'Oswald',sans-serif;font-weight:500;font-size:51px;line-height:1;color:var(--white);letter-spacing:-.5px}
.tagline{position:absolute;left:49px;top:282px;font-family:'Oswald',sans-serif;font-weight:500;font-size:11.5px;color:var(--white)}
.search{position:absolute;left:49px;top:332px;width:190px;height:27px;background:var(--white);border:1px solid #ccc}
.search svg{position:absolute;right:9px;top:5px}
.subscribe{position:absolute;left:49px;top:391px;font-family:'Lato',sans-serif;font-size:12px;line-height:25px;list-style:none}
.popular{position:absolute;left:49px;top:473px;font-family:'Lato',sans-serif}
.popular h3{font-weight:400;font-size:14px;color:var(--white);margin-bottom:8px}
.popular ul{list-style:none;font-size:12px;line-height:25.5px}
.popular li{padding-left:20px;position:relative}
.popular li::before{content:"";position:absolute;left:10px;top:11px;width:4px;height:4px;border-radius:50%;background:var(--white)}
.topbar{position:absolute;left:255px;top:0;width:783px;height:49px;background:var(--topbar)}
.band{position:absolute;left:255px;top:49px;width:783px;height:37px;background:var(--band)}
.nav{position:absolute;left:600px;top:14px;display:flex;gap:20px;align-items:center;height:22px}
.nav .label{font-family:'Lato',sans-serif;font-weight:700;font-size:9px;color:#0d0d0d}
.main{position:absolute;left:296px;top:126px;width:630px}
.post-image{display:block;width:509px;height:339px;background:linear-gradient(135deg,#6b4a30 0%,#3a2a20 45%,#1a1a1c 100%)}
.post{position:absolute;left:0;width:630px}
.post h2{font-family:'Aleo',serif;font-weight:400;font-size:31px;color:var(--ink);line-height:1}
.meta{font-family:Arial,sans-serif;font-size:10.5px;color:var(--ink);margin-top:9px}
.post p{font-size:13px;line-height:19.5px;color:var(--body);margin-top:17px}
.post p+p{margin-top:9px}
.more{font-size:13.5px}
.pager{position:absolute;left:574px;top:1099px;font-family:'Lato',sans-serif;font-size:18px;color:var(--muted)}
.older{position:absolute;left:843px;top:1094px;font-family:'Lato',sans-serif;font-weight:700;font-size:18px}
.footer{position:absolute;left:296px;top:1139px;font-family:'Lato',sans-serif;font-size:11.5px;line-height:15px;color:var(--muted)}
</style>
</head>
<body>
<aside class="sidebar">
  <div class="sidebar-photo" role="img" aria-label="Dusky mountain road stretching into the distance"></div>
  <div class="avatar" role="img" aria-label="Author portrait"></div>
  <h1 class="site-name">Tavelkin</h1>
  <p class="tagline">Rumblings of a coder and a late night owl</p>
  <div class="search">
    <svg width="16" height="16" viewBox="0 0 16 16" fill="none" stroke="#111" stroke-width="1.6"><circle cx="6.5" cy="6.5" r="5"/><path d="M10.2 10.2 15 15"/></svg>
  </div>
  <ul class="subscribe">
    <li><a href="#">Subscribe Via Email</a></li>
    <li><a href="#">Subscribe Via RSS</a></li>
  </ul>
  <section class="popular">
    <h3>Popular Posts</h3>
    <ul>
      <li><a href="#">Token-Based PubSub</a></li>
      <li><a href="#">Manual Subscriptions</a></li>
      <li><a href="#">Permission-Based PubSub</a></li>
      <li><a href="#">XSub Instead of Sub</a></li>
    </ul>
  </section>
</aside>

<header class="topbar">
  <nav class="nav">
    <svg width="20" height="18" viewBox="0 0 20 18" aria-label="Home"><path d="M10 1 1 9h3v8h4v-5h4v5h4V9h3z" fill="#0d0d0d"/></svg>
    <svg width="16" height="18" viewBox="0 0 16 18" aria-label="About"><circle cx="8" cy="5" r="4.5" fill="#0d0d0d"/><path d="M0 18c0-6 3-8 8-8s8 2 8 8z" fill="#0d0d0d"/></svg>
    <span class="label">Chirper</span>
    <span class="label">Linkwork</span>
    <span class="label">Plusring</span>
    <span class="label">Codenest</span>
    <svg width="20" height="14" viewBox="0 0 20 14" aria-label="Email"><rect x="1" y="1" width="18" height="12" fill="none" stroke="#0d0d0d" stroke-width="2"/><path d="M1 1l9 7 9-7" fill="none" stroke="#0d0d0d" stroke-width="2"/></svg>
  </nav>
</header>
<div class="band"></div>

<main class="main">
  <div class="post-image" role="img" aria-label="Person holding a phone in front of a laptop on a wooden desk"></div>

  <article class="post" style="top:366px">
    <h2>What Did you Said?</h2>
    <p class="meta">BY <a href="#">Tavelkin</a> ON OCT 15, 2014, TAGGED: <a href="#">Token</a>, <a href="#">Code</a></p>
    <p>Lorem Ipsum has been the industry's standard dummy text ever since the 1500s, when an unknown printer took a galley of type and scrambled it to make a type specimen book. It has survived not only five centuries, but also the leap into electronic typesetting, remaining essentially unchanged.</p>
    <p>It was popularised in the 1960s with the release of Markfold sheets containing Lorem Ipsum passages, and more recently with desktop publishing software like Quillset Composer including versions of Lorem Ipsum.... &nbsp;<a class="more" href="#">Continue reading</a></p>
  </article>

  <article class="post" style="top:643px">
    <h2>It Never Happened!</h2>
    <p class="meta">BY <a href="#">Tavelkin</a> ON OCT 15, 2014, TAGGED: <a href="#">Token</a>, <a href="#">Code</a></p>
    <p>Lorem Ipsum has been the industry's standard dummy text ever since the 1500s, when an unknown printer took a galley of type and scrambled it to make a type specimen book. It has survived not only five centuries, but also the leap into electronic typesetting, remaining essentially unchanged.</p>
    <p>It was popularised in the 1960s with the release of Markfold sheets containing Lorem Ipsum passages, and more recently with desktop publishing software like Quillset Composer including versions of Lorem Ipsum.... &nbsp;<a class="more" href="#">Continue reading</a></p>
  </article>
</main>

<p class="pager">1/2</p>
<a class="older" href="#">older...</a>
<footer class="footer">
  <p>Copyright Tavelkin. © 2014 • All rights reserved.</p>
  <p>Proudly published with Inkpage.</p>
</footer>
</body>
</html>
```